HR consultancy website - Wordpress Design Project

We need a wordpress design for a new company based in Belgium called Brivolane. We propose HR consultancy services focused on employees' engagement (motivation). We target corporations from 100 to 1000+ employees mainly in Europe.
We need a new design for our existing website (www.brivolane.eu).
We find the current design too static and outdated and we are looking for a more appealing look & feel.
Nevertheless, it has also to be sober.
The colours of the logo (dark blue, purple and light grey) should be preferrably used.
The content structure and the texts remain the same.

Target Market(s)

HR managers, general managers of SME's, higher education

Industry/Entity Type

It Company

Requirements
Must have
• No specific functionalities, except a contact form.

```html
<!DOCTYPE html>
<html lang="en">
<head>
<meta charset="utf-8">
<title>Brivolane – Foster performance by engaging employees</title>
<link rel="stylesheet" href="https://fonts.googleapis.com/css2?family=Bree+Serif&family=Montserrat:wght@400;500&family=Open+Sans:wght@600&display=swap">
<style>
  :root {
    --navy: #0b3c8c;
    --magenta: #c8256a;
    --magenta-light: #e0357f;
    --pink-soft: #eaa6c4;
    --logo-grey: #c5bfb8;
    --text: #555555;
    --text-dark: #333333;
    --panel: #f2f2f2;
    --line: #e2e2e2;
    --white: #ffffff;
  }
  * { margin: 0; padding: 0; box-sizing: border-box; }
  html, body { width: 1200px; height: 1051px; overflow: hidden; }
  body {
    position: relative;
    background: radial-gradient(ellipse at 50% 0%, #f4f4f4 0%, var(--white) 60%);
    font-family: "Montserrat", sans-serif;
    color: var(--text);
  }
  .top-bar { position: absolute; left: 0; top: 0; width: 1200px; height: 6px; background: var(--navy); }

  .brand {
    position: absolute; left: 140px; top: 62px;
    font-family: "Montserrat", sans-serif; font-weight: 400;
    font-size: 52px; letter-spacing: 2px; color: var(--logo-grey);
    display: flex; align-items: center; gap: 14px;
  }
  .brand-mark { width: 16px; height: 16px; background: var(--navy); }

  .contact-info { position: absolute; right: 141px; top: 28px; text-align: right; font-size: 14px; color: #777; }
  .contact-info .phone-line { display: flex; align-items: baseline; justify-content: flex-end; gap: 6px; }
  .contact-info .phone { font-size: 22px; font-weight: 500; color: #111; }
  .contact-info .email-line { margin-top: 2px; margin-right: 12px; }
  .contact-info .email { color: var(--magenta); }
  .phone-icon { position: absolute; left: 775px; top: 34px; width: 44px; height: 54px; }

  .main-nav { position: absolute; left: 648px; top: 121px; display: flex; gap: 4px; }
  .main-nav a {
    display: flex; align-items: center; justify-content: center;
    width: 135px; height: 42px; padding-left: 18px;
    color: var(--white); text-decoration: none; font-size: 16px;
    background: linear-gradient(180deg, #1b5fc4 0%, var(--navy) 100%);
    clip-path: polygon(26px 0, 100% 0, 100% 100%, 0 100%, 10px 40%);
  }

  .hero {
    position: absolute; left: 140px; top: 163px; width: 919px; height: 360px;
    background: var(--white); box-shadow: 0 0 6px rgba(0,0,0,0.18);
  }
  .hero-inner { position: absolute; left: 10px; top: 11px; width: 900px; height: 339px; background: var(--panel); }
  .hero-photo {
    position: absolute; right: 0; top: 0; width: 522px; height: 339px;
    background: linear-gradient(90deg, var(--panel) 0%, #dfe9f4 30%, #c9d9ec 65%, #e8eef5 100%);
  }
  .hero-copy { position: absolute; left: 48px; top: 20px; width: 344px; text-align: center; }
  .hero-title { font-family: "Bree Serif", serif; font-weight: 400; font-size: 46px; color: var(--magenta); line-height: 58px; }
  .hero-rule { height: 1px; background: var(--line); margin: 8px 0 26px; }
  .hero-tagline { font-family: "Open Sans", sans-serif; font-weight: 600; font-size: 22px; line-height: 29px; color: var(--text-dark); }
  .hero-button {
    display: inline-block; margin-top: 34px; width: 147px; height: 35px; line-height: 35px;
    border-radius: 18px; background: var(--pink-soft); color: var(--white);
    font-family: "Bree Serif", serif; font-weight: 400; font-size: 20px; text-decoration: none;
  }

  .features { position: absolute; left: 140px; top: 540px; width: 920px; display: flex; }
  .feature { position: relative; width: 234px; height: 216px; padding-top: 24px; }
  .feature + .feature { border-left: 1px solid var(--line); }
  .feature-ribbon {
    position: relative; height: 42px; width: 217px; margin-left: 0;
    background: linear-gradient(180deg, var(--magenta-light) 0%, #b51f5e 100%);
    clip-path: polygon(0 0, 95% 0, 100% 50%, 95% 100%, 0 100%);
    font-family: "Bree Serif", serif; font-weight: 400; font-size: 29px; color: var(--white);
    line-height: 42px; padding-left: 54px; white-space: nowrap;
  }
  .feature + .feature .feature-ribbon { margin-left: 6px; }
  .feature-number {
    position: absolute; left: 0; top: 23px; width: 44px; height: 44px; border-radius: 50%;
    background: var(--navy); border: 3px solid var(--white); box-shadow: 0 0 0 1px #c9cbd6;
    color: var(--white); font-size: 23px; text-align: center; line-height: 38px; z-index: 1;
  }
  .feature + .feature .feature-number { left: 6px; }
  .feature-text {
    margin: 26px 10px 0; text-align: center; font-size: 14.5px; line-height: 20.5px;
    color: var(--text); hyphens: auto;
  }

  .cta-band {
    position: absolute; left: 140px; top: 810px; width: 920px; height: 92px;
    background: radial-gradient(ellipse at 50% 10%, #f1f1f1 0%, rgba(255,255,255,0) 70%);
  }
  .cta-heading { position: absolute; left: 0; top: 836px; width: 1200px; text-align: center; font-family: "Bree Serif", serif; font-weight: 400; font-size: 25px; color: var(--text); }
  .cta-button {
    position: absolute; left: 491px; top: 895px; width: 219px; height: 68px; border-radius: 34px;
    background: linear-gradient(180deg, #7a7a7a 0%, #3a3a3a 45%, #0d0d0d 55%, #222 100%);
    box-shadow: 0 3px 5px rgba(0,0,0,0.3), inset 0 0 0 2px #999;
    color: var(--white); text-decoration: none; text-align: center; line-height: 68px;
    font-family: "Bree Serif", serif; font-weight: 400; font-size: 26px;
  }

  .site-footer { position: absolute; left: 140px; top: 1004px; width: 919px; border-top: 1px solid var(--line); text-align: center; padding-top: 16px; font-size: 15px; color: var(--text); }
</style>
</head>
<body>
  <div class="top-bar"></div>

  <header>
    <div class="brand"><span>BRIVOLANE</span><span class="brand-mark"></span></div>

    <svg class="phone-icon" viewBox="0 0 44 54" aria-hidden="true">
      <path d="M12 4 C4 8 2 22 8 36 C12 46 22 50 30 46 L26 38 C21 40 17 36 15 30 C12 22 13 16 18 14 Z" fill="none" stroke="#222" stroke-width="3"/>
      <path d="M30 46 C36 48 42 44 42 38" fill="none" stroke="#222" stroke-width="2"/>
    </svg>
    <div class="contact-info">
      <div class="phone-line"><span>Contact us on</span><span class="phone">(02) 5817 2039</span></div>
      <div class="email-line">or email us <span class="email">hello@brivolane.eu</span></div>
    </div>

    <nav class="main-nav">
      <a href="#mission">Our Mission</a>
      <a href="#about">About</a>
      <a href="#contact">Contact</a>
    </nav>
  </header>

  <section class="hero">
    <div class="hero-inner">
      <div class="hero-photo" role="img" aria-label="Photo of three smiling office colleagues working together at a laptop"></div>
      <div class="hero-copy">
        <h1 class="hero-title">Brivolane</h1>
        <div class="hero-rule"></div>
        <p class="hero-tagline">FOSTER PERFORMANCE<br>BY<br>ENGAGING EMPLOYEES</p>
        <a class="hero-button" href="#mission">Our Mission</a>
      </div>
    </div>
  </section>

  <section class="features">
    <article class="feature">
      <span class="feature-number">1</span>
      <h2 class="feature-ribbon">Evaluation</h2>
      <p class="feature-text">Only between 13 and 21% of employees are actively engaged in their job.</p>
    </article>
    <article class="feature">
      <span class="feature-number">2</span>
      <h2 class="feature-ribbon">Strategy</h2>
      <p class="feature-text">Brivolane helps corporate leaders get the best contribution from employees.</p>
    </article>
    <article class="feature">
      <span class="feature-number">3</span>
      <h2 class="feature-ribbon">Process</h2>
      <p class="feature-text">Our ERM tool creates an HR engagement cycle to encourage line managers to take initiatives and to enhance the engagement of their team members.</p>
    </article>
    <article class="feature">
      <span class="feature-number">4</span>
      <h2 class="feature-ribbon">Impact</h2>
      <p class="feature-text">Our ERM tool measures impact by creating an index which can then be used for comparison over time.</p>
    </article>
  </section>

  <div class="cta-band"></div>
  <h2 class="cta-heading">Boost Your Company's Performance!</h2>
  <a class="cta-button" href="#contact">Contact Us</a>

  <footer class="site-footer">Copyright © 2012 Brivolane. All Rights Reserved.</footer>
</body>
</html>
```